BOLD & MINIMALIST DESIGN NEEDED

We want a very bold but minimalistic business card design that is impactful and utilizes both sides of the business card. Our current logo is included for your use.

We want bold fonts and good use of negative space. We don't want the logo to overpower the design.

Target Market(s)

Professionals who are building new commercial buildings.

Industry/Entity Type

Construction

Contact Information for Business Card

Name, Title, email, office phone, cell phone, website

Font styles to use
Serif
Sans Serif

Requirements
Must have
• Bold design!

```html
<!DOCTYPE html>
<html lang="en">
<head>
<meta charset="utf-8">
<title>Ridgeline Build — Business Card</title>
<link rel="stylesheet" href="https://fonts.googleapis.com/css2?family=Arimo:wght@400;700&display=swap">
<style>
  :root {
    --bg: #e3e3e3;
    --card-white: #ffffff;
    --ink: #1d1d1d;
    --text-grey: #4a4a4a;
    --rule: #cfcfcf;
    --green: #8cc63f;
    --green-light: #c4e39a;
    --charcoal: #232323;
    --back-top: #3c3c3c;
    --back-bottom: #2c2c2c;
  }
  * { box-sizing: border-box; margin: 0; padding: 0; }
  html, body { width: 1200px; height: 1200px; overflow: hidden; }
  body {
    background: var(--bg);
    font-family: "Arimo", Arial, sans-serif;
    position: relative;
  }
  .card {
    position: absolute;
    left: 256px;
    width: 688px;
    height: 394px;
    border-radius: 20px;
    overflow: hidden;
  }
  .card--front { top: 158px; background: var(--card-white); }
  .card--back {
    top: 652px;
    background: linear-gradient(180deg, var(--back-top), var(--back-bottom));
    display: flex;
    align-items: center;
    justify-content: center;
  }

  .brand {
    display: flex;
    align-items: center;
    gap: 12px;
    font-weight: 700;
    letter-spacing: 1px;
    text-transform: uppercase;
  }
  .brand__mark { background: var(--green); flex: none; }
  .brand--front {
    position: absolute;
    top: 120px;
    left: 410px;
    font-size: 34px;
    color: var(--ink);
  }
  .brand--front .brand__mark { width: 22px; height: 22px; }
  .brand--back { font-size: 60px; color: #ffffff; gap: 18px; }
  .brand--back .brand__mark { width: 38px; height: 38px; }

  .person { position: absolute; left: 45px; top: 214px; }
  .person__name {
    font-size: 27px;
    font-weight: 700;
    color: var(--ink);
    letter-spacing: 0.3px;
  }
  .person__title {
    font-size: 15px;
    color: var(--green);
    margin-top: 3px;
  }
  .divider {
    position: absolute;
    left: 45px;
    top: 274px;
    width: 596px;
    height: 1px;
    background: var(--rule);
  }
  .contacts {
    position: absolute;
    left: 41px;
    top: 283px;
    list-style: none;
  }
  .contacts li {
    display: flex;
    align-items: center;
    height: 20.5px;
    font-size: 16px;
    color: var(--text-grey);
  }
  .contacts svg { width: 14px; height: 14px; margin-right: 12px; flex: none; }

  .footer-band { position: absolute; left: 0; bottom: 0; width: 688px; height: 34px; }
  .website {
    position: absolute;
    right: 40px;
    bottom: 8px;
    font-size: 16px;
    color: var(--ink);
  }
</style>
</head>
<body>

<section class="card card--front" aria-label="Business card front">
  <div class="brand brand--front"><span class="brand__mark"></span>Ridgeline Build</div>

  <div class="person">
    <h1 class="person__name">MARK ELLISON</h1>
    <p class="person__title">President</p>
  </div>
  <div class="divider"></div>

  <ul class="contacts">
    <li>
      <svg viewBox="0 0 24 24" aria-hidden="true"><path fill="#1d1d1d" d="M6.6 10.8a15.1 15.1 0 0 0 6.6 6.6l2.2-2.2c.3-.3.7-.4 1-.2 1.1.4 2.3.6 3.6.6.6 0 1 .4 1 1V20c0 .6-.4 1-1 1A17 17 0 0 1 3 4c0-.6.4-1 1-1h3.5c.6 0 1 .4 1 1 0 1.3.2 2.5.6 3.6.1.3 0 .7-.2 1z"/></svg>
      555-201-4830
    </li>
    <li>
      <svg viewBox="0 0 24 24" aria-hidden="true"><rect x="6" y="1.5" width="12" height="21" rx="2" fill="none" stroke="#1d1d1d" stroke-width="2"/><rect x="10" y="18" width="4" height="1.6" fill="#1d1d1d"/></svg>
      555-201-7716
    </li>
    <li>
      <svg viewBox="0 0 24 24" aria-hidden="true"><rect x="2" y="5" width="20" height="14" fill="#1d1d1d"/><path d="M2.5 5.5 12 13l9.5-7.5" fill="none" stroke="#ffffff" stroke-width="1.6"/></svg>
      info@ridgelinebuild.com
    </li>
  </ul>

  <svg class="footer-band" viewBox="0 0 688 34" preserveAspectRatio="none" aria-hidden="true">
    <defs>
      <linearGradient id="bandGreen" x1="0" x2="1" y1="0" y2="0">
        <stop offset="0" stop-color="#8cc63f"/>
        <stop offset="0.6" stop-color="#c4e39a"/>
        <stop offset="1" stop-color="#8cc63f"/>
      </linearGradient>
    </defs>
    <rect x="0" y="0" width="688" height="34" fill="url(#bandGreen)"/>
    <path d="M0 0 H460 Q448 2 432 14 H0 Z" fill="#232323"/>
    <path d="M0 14 H432 Q422 18 410 20 H0 Z" fill="#ffffff"/>
  </svg>
  <p class="website">www.ridgelinebuild.com</p>
</section>

<section class="card card--back" aria-label="Business card back">
  <div class="brand brand--back"><span class="brand__mark"></span>Ridgeline Build</div>
</section>

</body>
</html>
```